Modern Gin Label - Australian Distillery

Tallow Distillery is working on our first release: Reef Glow Gin, a bold and distinctly Australian small-batch craft gin. We are seeking a professional label design that is modern, fun, and visually highlights our use of unique native botanicals. The label must be print-ready, adhere to Australian spirits labelling regulations, and incorporate room for batch and bottle numbers.
We will be printing a label to go onto the VessoKraft 700ml Regal Bottle (VK700R-D), and all files must be prepared to industry standards including dielines, bleed, and print finishes (emboss/foil layers as needed).
________________________________________
Design Objectives
• Modern and Fun: Clean layout, contemporary typefaces, and bright, engaging design
• Botanical-Inspired: Creative use of natural elements or abstract botanical references
• Premium, Craft Feel
• Compliant and Practical: All mandatory label elements included, space for batch/bottle numbers
Bottle & Label Specs (Spec Sheet Attached)
• Bottle: VessoKraft 700ml Regal Bottle
o Code: VK700R-D
o Height: 252 ± 1.8 mm
o Diameter: 83.0 ± 1.7 mm
o Label Panel Height: 155.9 mm
** Maximum Label Height 130mm**
o Finish: Cork, 23 mm
• Label Type: Single Front Label up to 2/3 of bottle circumference (preferred) or Front and Back Label
• Logo: To be placed prominently at the top of the label (supplied - resize as apropriate)
Botanical Composition:
Juniper
Coriander Seed
Angelica Root
Lemon Aspen
Desert Lime
Lemon Peel
Mandarin Peel
River Mint
Orris Root
Macadamia Nut
Cassia Bark
Elderflower
Lemon Verbena
Cardamom
Pepperberry
Note: If space or design is tight, designers are encouraged to feature or highlight select botanicals rather than attempt to represent all 15. Interpret botanicals visually, illustratively, texturally, or through abstract form, depending on your creative direction.
Tasting Notes (Optional inclusion – can be used on the back label or subtly featured as a tagline or paragraph - feel free to shorten)
Tasting Notes – Reef Glow Gin
Bright and evocative, Reef Glow Gin opens with a clean, classic juniper backbone. A vibrant citrus medley follows—fresh lemon peel, lemon aspen, and dried mandarin create a layered zestiness, with native desert lime’s tart dryness adding bite. River mint and lemon verbena add herbal lift, with soft floral elderflower and buttery macadamia for depth. A warm spice finish from coriander, cardamom, cassia bark, and pepperberry rounds out this bright, aromatic, and subtly spicy modern Australian gin.
Mandatory Label Inclusions
In compliance with Australian distilled spirits regulations, the label must include:
• Product Name: Reef Glow Gin
• Alcohol Content: 40% ALC/VOL
• Volume: 700 mL
• Standard Drinks: Approx. 22 standard drinks
• Producer Statement:
PRODUCED BY MARLOW BOTTLERS, 2287 KESTREL PARK RD, DARLINGTON 5042
FOR TALLOW DISTILLERY
• Country of Origin: Product of Australia
• Pregnancy Warning: Include QORBY-approved pictogram (Supplied)
• Lot Identification Area:
Provide a blank space marked:
Batch No. ____ | Bottle No. ____
• Barcode (Supplied)
• Allergen Advice (Contains Macadamia Nut)
• Website: tallowdistillery-example.com.au
Optional Elements (if space and layout permit):
• Short story or brand ethos (can be supplied on request)
• Suggested serve line (e.g., “Ideal for sipping neat, with tonic, or in citrus-forward cocktails.”)
• Craft Distilled icon or statement
• Sip steady Logo – Your Choice (Supplied)
• Recycling Logo
Technical Requirements
• Final Output: Print-ready PDF + native design file (AI preferred)
• Colour Mode: CMYK
• Bleed: 3 mm
• Safe Zone: Clearly defined
• Cut Lines: Clearly marked die line
• Foil: Use spot colour layers for special finishes
• Fonts: Outlined or included in package
• Mock-up: Provide a rendered bottle mock up with applied label
Deliverables
• Front label artwork (and back/wrap if applicable)
• Print-ready PDF
• Adobe Illustrator (or editable vector format) source file
• Separate files or layers for foil/emboss
• Dieline file
• Bottle mockup
NOTES:
1. I have included the QORBY Standards document for the sizes of the pregnancy logo
2. for the Tallow Distillery logo, I am happy for you to put a border around it or even use it without the blue background depending on the design.
Target Market(s)
People that are looking for a great tasting Gin, not too serious and loads fun.
Industry/Entity Type
Distilled Spirits
Requirements
Must have
- In compliance with Australian distilled spirits regulations, the label must include: • Product Name: Reef Glow Gin • Alcohol Content: 40% ALC/VOL • Volume: 700 mL • Standard Drinks: Approx. 22 standard drinks • Producer Statement: PRODUCED BY MARLOW BOTTLERS, 2287 KESTREL PARK RD, DARLINGTON 5042 FOR TALLOW DISTILLERY • Country of Origin: Product of Australia • Pregnancy Warning: Include QORBY-approved pictogram (Supplied) • Lot Identification Area: Provide a blank space marked: Batch No. ____ | Bottle No. ____ • Barcode (Supplied) • Allergen Advice (Contains Macadamia Nut) • Website: tallowdistillery-example.com.au

```html
<!DOCTYPE html>
<html lang="en">
<head>
<meta charset="utf-8">
<title>Reef Glow Gin – Label</title>
<link rel="stylesheet" href="https://fonts.googleapis.com/css2?family=Antonio:wght@300;400;600&family=Oswald:wght@300;400;600&family=Open+Sans:wght@400;700&display=swap">
<style>
  :root {
    --page: #efedeb;
    --label: #2b2b2d;
    --label-edge: #232325;
    --white: #ffffff;
    --soft-white: #dcdcdc;
    --gold: #b89a3a;
    --gold-deep: #7d6a2a;
    --gold-bright: #d8b43a;
    --warn-red: #d2232a;
  }
  * { box-sizing: border-box; margin: 0; padding: 0; }
  html, body { width: 1200px; height: 1200px; overflow: hidden; }
  body {
    background: var(--page);
    font-family: "Oswald", "Arial Narrow", sans-serif;
    position: relative;
  }
  .label {
    position: absolute;
    left: 90px; top: 280px;
    width: 1020px; height: 640px;
    background: var(--label);
    display: grid;
    grid-template-columns: 270px 480px 270px;
    color: var(--white);
    overflow: hidden;
  }
  /* Left panel: tasting notes & lot area */
  .panel-side {
    position: relative;
    padding: 110px 30px 30px;
  }
  .tasting-notes {
    font-family: "Oswald", sans-serif;
    font-weight: 300;
    font-size: 13px;
    line-height: 1.75;
    text-transform: uppercase;
    color: var(--soft-white);
  }
  .tasting-notes h3 {
    font-weight: 600;
    font-size: 14px;
    letter-spacing: 1px;
    margin-bottom: 8px;
    color: var(--white);
  }
  .side-botanical {
    position: absolute;
    left: 30px; right: 30px; top: 360px; height: 170px;
    background: linear-gradient(180deg, rgba(184,154,58,0) 0%, rgba(184,154,58,0.35) 60%, rgba(125,106,42,0.2) 100%);
  }
  .lot-area {
    position: absolute;
    left: 30px; bottom: 34px;
    background: var(--soft-white);
    color: var(--label);
    font-size: 12px;
    font-weight: 400;
    padding: 5px 10px;
    letter-spacing: 0.5px;
  }
  /* Centre panel */
  .panel-front {
    position: relative;
    text-align: center;
  }
  .brand {
    position: absolute;
    top: 38px; left: 0; right: 0;
    display: flex; flex-direction: column; align-items: center; gap: 10px;
  }
  .brand-mark {
    width: 44px; height: 44px;
    background: var(--gold-bright);
  }
  .brand-name {
    font-family: "Open Sans", sans-serif;
    font-weight: 700;
    font-size: 15px;
    color: var(--gold-bright);
  }
  .front-botanical {
    position: absolute;
    left: 30px; right: 20px; top: 290px; bottom: 0;
    background: radial-gradient(ellipse at 55% 65%, rgba(184,154,58,0.6) 0%, rgba(125,106,42,0.35) 55%, rgba(43,43,45,0) 85%);
  }
  .product-name {
    position: absolute;
    top: 165px; left: 0; right: 0;
    font-family: "Antonio", sans-serif;
    color: var(--white);
    line-height: 1;
  }
  .product-name .sub {
    display: block;
    font-weight: 400;
    font-size: 78px;
    letter-spacing: 1px;
  }
  .product-name .main {
    display: block;
    font-weight: 600;
    font-size: 210px;
    letter-spacing: 8px;
    margin-top: 8px;
  }
  .origin {
    position: absolute;
    left: 56px; right: 56px; bottom: 68px;
    font-weight: 600;
    font-size: 17px;
    letter-spacing: 9px;
    text-align: center;
  }
  .front-specs {
    position: absolute;
    left: 60px; right: 60px; bottom: 28px;
    display: flex; justify-content: space-between;
    font-weight: 400;
    font-size: 15px;
    color: var(--soft-white);
  }
  /* Right panel: compliance */
  .compliance {
    padding: 110px 30px 30px;
    font-size: 13px;
    line-height: 1.7;
    text-transform: uppercase;
    color: var(--soft-white);
    font-weight: 300;
  }
  .compliance .producer { text-align: center; margin-bottom: 22px; }
  .compliance .rule { border-top: 1px solid var(--soft-white); margin: 12px 0; }
  .compliance .strong { font-weight: 600; color: var(--white); }
  .warning {
    display: flex; align-items: center; gap: 10px;
    background: var(--white);
    color: var(--label);
    padding: 6px 8px;
    margin-top: 16px;
    text-transform: none;
    line-height: 1.3;
    font-size: 11px;
  }
  .warning-title { color: var(--warn-red); font-weight: 600; }
  .warning-pictogram {
    width: 34px; height: 34px; flex: none;
    border: 3px solid var(--warn-red); border-radius: 50%;
  }
  .responsible {
    display: flex; align-items: center; gap: 10px;
    margin-top: 16px;
    text-transform: none;
  }
  .recycle-mark {
    width: 26px; height: 26px; border-radius: 50%;
    border: 2px solid var(--soft-white);
  }
  .sip-steady {
    background: var(--white); color: var(--label);
    font-weight: 400; font-size: 12px; padding: 3px 8px;
  }
</style>
</head>
<body>
  <main class="label">
    <section class="panel-side">
      <div class="tasting-notes">
        <h3>Tasting Notes</h3>
        <p>Reef Glow Gin opens with clean juniper. Fresh lemon peel, lemon aspen and mandarin create layered zest, with desert lime's tart bite. River mint and soft elderflower lift, buttery macadamia adds depth, and a warm aromatic spice finish lingers.</p>
      </div>
      <div class="side-botanical" role="img" aria-label="Gold line illustration of native botanicals"></div>
      <div class="lot-area">Batch No. ____ | Bottle No. ____</div>
    </section>

    <section class="panel-front">
      <div class="brand">
        <span class="brand-mark"></span>
        <span class="brand-name">Tallow Distillery</span>
      </div>
      <div class="front-botanical" role="img" aria-label="Gold line illustration of native flowers and botanicals"></div>
      <h1 class="product-name">
        <span class="sub">REEF GLOW</span>
        <span class="main">GIN</span>
      </h1>
      <p class="origin">PRODUCT OF AUSTRALIA</p>
      <div class="front-specs">
        <span>40.0% ALC/VOL</span>
        <span>VOL 700ML</span>
      </div>
    </section>

    <section class="compliance">
      <p class="producer">Produced by Marlow Bottlers,<br>2287 Kestrel Park Rd, Darlington 5042<br><span class="strong">For Tallow Distillery</span><br>Contains Macadamia Nut</p>
      <div class="rule"></div>
      <p>Approx. 22 Standard Drinks</p>
      <div class="rule"></div>
      <p class="strong">40.0% ALC/VOL</p>
      <p class="strong">tallowdistillery-example.com.au</p>
      <div class="warning">
        <span class="warning-pictogram" role="img" aria-label="Pregnancy warning pictogram"></span>
        <span><span class="warning-title">PREGNANCY WARNING</span><br>Alcohol can cause lifelong harm to your baby</span>
      </div>
      <div class="responsible">
        <span class="recycle-mark" role="img" aria-label="Recycling mark"></span>
        <span class="sip-steady">Sip steady</span>
      </div>
    </section>
  </main>
</body>
</html>
```